Interior Design/ decoration business card design

This card is for my Interior Design and Decoration business and later I will also be selling homewares. I would like the card to be very simple in design and like either white, duck egg blue , aquas or metallics on a flat mat card excellent quality card. It needs to be well designed as that is my field. I dont like fuss, the simpler the better. I would like a styalised wren under the name wren if possible. SIMPLE, STYLISH, CLASSIC, TASTEFUL

Target Market(s)

40 + year olds who are building or rennovating.

Industry/Entity Type

Business

Contact Information for Business Card

Wren
styling, design, homeware

Maren Tulloch
p 0437165093
e maren@wrenliving.com.au
w wrenliving.com.au

Requirements
Must have
• very simple, stylish, classic, sophisticated. Simple and easy to read text that is a print similar to attached image. I like simple round A's though not as in attached image.

Double sided. It wont save as double sided for some reason!!
Should not have
• not too much colour, No animated / cartoon pictures.

```html
<!DOCTYPE html>
<html lang="en">
<head>
<meta charset="utf-8">
<title>Wren — Business Card</title>
<link href="https://fonts.googleapis.com/css2?family=Roboto:wght@100;300;400&display=swap" rel="stylesheet">
<style>
  :root {
    --backdrop: #eeeeec;
    --duck-egg: #bfe2e0;
    --duck-egg-deep: #a9d6d4;
    --card-white: #ffffff;
    --teal-text: #8cc3c0;
    --white-text: #ffffff;
    --muted-text: #6f7b7b;
  }
  * { margin: 0; padding: 0; box-sizing: border-box; }
  html, body {
    width: 1200px;
    height: 800px;
    overflow: hidden;
    background: var(--backdrop);
    font-family: "Roboto", Arial, sans-serif;
  }
  .sheet {
    width: 1200px;
    height: 800px;
    display: flex;
    align-items: center;
    justify-content: center;
    gap: 60px;
  }
  .card {
    position: relative;
    width: 525px;
    height: 300px;
    box-shadow: 0 6px 18px rgba(0,0,0,0.12);
  }
  .card--front {
    background: linear-gradient(135deg, var(--duck-egg) 0%, var(--duck-egg-deep) 100%);
  }
  .card--back {
    background: var(--card-white);
  }
  .tagline {
    position: absolute;
    top: 40px;
    left: 44px;
    font-weight: 300;
    font-size: 19px;
    letter-spacing: 0.5px;
    color: var(--white-text);
  }
  .brand-name {
    position: absolute;
    top: 100px;
    left: 190px;
    font-weight: 100;
    font-size: 72px;
    letter-spacing: 2px;
    color: var(--white-text);
  }
  .contact {
    position: absolute;
    top: 62px;
    left: 170px;
    color: var(--teal-text);
  }
  .contact__name {
    font-weight: 400;
    font-size: 22px;
    margin-bottom: 14px;
  }
  .contact__line {
    font-weight: 300;
    font-size: 13px;
    line-height: 19px;
  }
  .abn {
    position: absolute;
    top: 30px;
    right: 26px;
    font-weight: 300;
    font-size: 12px;
    color: var(--muted-text);
  }
</style>
</head>
<body>
  <main class="sheet">
    <section class="card card--front">
      <p class="tagline">Decoration | Styling | Design</p>
      <p class="brand-name">wren</p>
    </section>
    <section class="card card--back">
      <p class="abn">ABN: 48302617954</p>
      <div class="contact">
        <p class="contact__name">Maren Tulloch</p>
        <p class="contact__line">0437 165 093</p>
        <p class="contact__line">maren@wrenliving.com.au</p>
        <p class="contact__line">wrenliving.com.au</p>
      </div>
    </section>
  </main>
</body>
</html>
```